One-Page Flat Design for SEO Company [2 DAYS]

We need a one-page flat design for our SEO company. Our current website is http://www.rankloft.com/. We are looking to completely re-design the site using new flat design techniques.
Below are some examples of the type of style we're going after:
http://quormel.com/
http://tobyrand.co.uk/
https://pentaly.co/
http://milesporter.me/
As you can see- flat, clean, minimal. It is very important you follow this type of style.
For colour scheme, you may use one of the pre-made colour palettes from here:
http://www.vornacle.com/blog/inspiration/24-flat-designs-with-compelling-color-palettes
I've attached a wireframe to be followed.
Hi,

```html
<!DOCTYPE html>
<html lang="en">
<head>
<meta charset="utf-8">
<title>RankLoft – SEO services that actually work</title>
<link rel="stylesheet" href="https://fonts.googleapis.com/css2?family=Source+Sans+3:wght@400;600&family=Arimo:wght@700&family=Roboto:wght@300&display=swap">
<style>
  :root {
    --header-blue: #428de0;
    --page-blue: #3d8fc0;
    --fold-light: #6ea2f2;
    --fold-shadow: #3570b4;
    --nav-active: #6b5139;
    --white: #ffffff;
    --device-dark: #4a4a4a;
    --device-mid: #8f8f8f;
  }
  * { margin: 0; padding: 0; box-sizing: border-box; }
  html, body {
    width: 1200px;
    height: 576px;
    overflow: hidden;
    background: var(--page-blue);
  }
  .page {
    position: relative;
    width: 1200px;
    height: 576px;
    background: var(--page-blue);
    color: var(--white);
  }
  .site-header {
    position: absolute;
    inset: 0 0 auto 0;
    height: 83px;
    background: var(--header-blue);
  }
  .brand {
    position: absolute;
    left: 150px;
    top: 17px;
    font-family: "Source Sans 3", sans-serif;
    line-height: 1;
  }
  .brand-name {
    display: block;
    font-size: 25px;
    font-weight: 400;
  }
  .brand-tagline {
    display: block;
    margin-top: 4px;
    font-size: 13px;
  }
  .main-nav {
    position: absolute;
    top: 32px;
    left: 628px;
    display: flex;
    font-family: "Arimo", sans-serif;
    font-size: 13px;
    font-weight: 700;
    list-style: none;
  }
  .main-nav li { margin-right: 18px; }
  .main-nav a {
    display: block;
    height: 22px;
    line-height: 22px;
    padding: 0 9px;
    color: var(--white);
    text-decoration: none;
  }
  .main-nav .is-active a {
    background: var(--nav-active);
    border-radius: 2px;
  }
  .page-fold {
    position: absolute;
    top: 0;
    right: 0;
  }
  .hero {
    position: absolute;
    top: 83px;
    left: 0;
    width: 1200px;
    text-align: center;
  }
  .hero-title {
    margin-top: 60px;
    margin-left: -12px;
    font-family: "Source Sans 3", sans-serif;
    font-weight: 600;
    font-size: 52px;
    letter-spacing: -1px;
    line-height: 58px;
  }
  .hero-lead {
    margin-top: 22px;
    font-family: "Roboto", sans-serif;
    font-weight: 300;
    font-size: 20px;
    line-height: 27px;
    letter-spacing: -0.6px;
  }
  .hero-devices {
    position: absolute;
    left: 347px;
    top: 298px;
    width: 436px;
    height: 248px;
    border-radius: 6px;
    background: linear-gradient(135deg, var(--device-dark) 0%, var(--device-mid) 50%, var(--device-dark) 100%);
  }
</style>
</head>
<body>
<div class="page">
  <header class="site-header">
    <div class="brand">
      <span class="brand-name">RankLoft</span>
      <span class="brand-tagline">A single Page Template</span>
    </div>
    <ul class="main-nav">
      <li class="is-active"><a href="#home">Home</a></li>
      <li><a href="#about">About</a></li>
      <li><a href="#packages">Packages</a></li>
      <li><a href="#services">Services</a></li>
      <li><a href="#other">Other</a></li>
      <li><a href="#contact">Contact</a></li>
    </ul>
  </header>

  <svg class="page-fold" width="40" height="84" viewBox="0 0 40 84" aria-hidden="true">
    <polygon points="40,48 40,84 13,48" fill="var(--fold-shadow)"/>
    <path d="M0 0 H40 V48 H13 Q0 48 0 35 Z" fill="var(--fold-light)"/>
  </svg>

  <section class="hero" id="home">
    <h1 class="hero-title">Finally, SEO services that actually work.</h1>
    <p class="hero-lead">Top-notch SEO services that are guaranteed to boost your search engine rankings.<br>100% Searchly-friendly.</p>
  </section>

  <div class="hero-devices" role="img" aria-label="Flat illustration of a laptop, tablet and phone with blank screens"></div>
</div>
</body>
</html>
```